Business card, PL Profile Cover Page & Postcard Flyer

For the Business card, we would like the following contents/texts.
Suggestions (not required) for the placements of contents:
The front
Company name with tagline (where love happens)
Full name
Title (Chief Executive or Managing Director)
Mobile number
Email address style: first.lastname@vombrily.com
And the back:
Company logo and full web address www.vombrily.com
Company UK address – Vombrily (Europe) Limited, Third Floor,
58 Corvane Road, London
N4K 7PQ (commas are not required)
In small or subtle print “registered in England No. 53xxxx”
Registered office: 9 Ellow Bank Yard, London, S62 4DT registered in England. Company no.
The look and fill should be simple, elegant, classy and luxurious.

PageLink Cover Image

We would like a design of our PageLink profile cover.
For the Cover Image – we would like you to use your initiative and creativity to ensure the style, look and feel are consistent with the company logo. We would like to see the company logo, and some texts with a background image, preferably with some illustration, however, an original work based on loyalty free photos or images can be acceptable.
We would like a cover text to appear on the cover image, “Love happens 2160 truths later, in less than 90 seconds. How can we make love happen for you? Visit www.vombrily.com”. Email info@vombrily.com

Postcard flyer

Like the Pagelink Cover Image, we would like you to use your initiative and creativity to ensure the style, look and feel are consistent with the logo you created for the company. We welcome illustration or original work based on loyalty free photos or images. Text/content wise we would like,
Company web address, logo, email (info@vombrily.com)
“Love happens 2,160 truths later, in less than 90 seconds. May we make love happen for you? Visit www.vombrily.com or email us now info@vombrily.com"

```html
<!DOCTYPE html>
<html lang="en">
<head>
<meta charset="utf-8">
<title>Vombrily Business Card</title>
<link rel="stylesheet" href="https://fonts.googleapis.com/css2?family=Source+Sans+3:wght@300;400;600;700&display=swap">
<style>
  :root {
    --page: #ecebe8;
    --card: #ffffff;
    --navy: #12465e;
    --green: #8cc63f;
    --ink: #4a4f52;
    --ink-dark: #222;
    --rule: #b9bfc2;
  }
  * { box-sizing: border-box; margin: 0; padding: 0; }
  html, body { width: 1200px; height: 720px; overflow: hidden; }
  body {
    background: var(--page);
    font-family: "Source Sans 3", Arial, sans-serif;
    color: var(--ink);
    position: relative;
  }
  .card {
    position: absolute;
    top: 205px;
    width: 540px;
    height: 310px;
    background: var(--card);
    box-shadow: 0 2px 10px rgba(0,0,0,0.12);
    overflow: hidden;
  }
  .card--front { left: 40px; }
  .card--back { left: 620px; }

  .brand { display: flex; align-items: center; gap: 16px; }
  .brand__mark {
    width: 46px; height: 46px; border-radius: 50%;
    background: var(--navy);
    flex: none;
  }
  .brand__name {
    font-weight: 300;
    font-size: 52px;
    letter-spacing: 3px;
    line-height: 1;
    color: var(--navy);
  }

  /* Front */
  .card--front .brand { position: absolute; left: 70px; top: 56px; }
  .holder {
    position: absolute; right: 300px; top: 170px; text-align: right;
  }
  .holder__name { font-weight: 700; font-size: 19px; color: var(--ink-dark); }
  .holder__title { font-size: 14px; color: var(--green); }
  .divider {
    position: absolute; left: 256px; top: 166px;
    width: 1px; height: 52px; background: var(--rule);
  }
  .contact {
    position: absolute; left: 272px; top: 168px;
    list-style: none; font-size: 14px; color: var(--ink);
  }
  .contact li { display: flex; align-items: center; gap: 8px; height: 24px; }
  .contact svg { width: 14px; height: 14px; fill: var(--ink); }
  .band-line {
    position: absolute; left: 0; right: 0; bottom: 62px;
    height: 3px; background: var(--green);
  }
  .band {
    position: absolute; left: 0; right: 0; bottom: 0;
    height: 56px; background: var(--navy);
  }

  /* Back */
  .card--back .brand { position: absolute; left: 90px; top: 46px; }
  .details {
    position: absolute; left: 0; right: 0; top: 128px;
    text-align: center; font-size: 15px; line-height: 1.3;
  }
  .details__heading { font-weight: 600; color: var(--navy); font-size: 15.5px; }
  .details__line { color: var(--ink); }
  .details__block + .details__block { margin-top: 6px; }
  .details__reg { margin-top: 10px; font-size: 14.5px; }
  .details__web {
    margin-top: 8px; font-weight: 600; font-size: 18px;
    letter-spacing: 1.5px; color: var(--ink-dark);
  }
</style>
</head>
<body>
  <section class="card card--front">
    <div class="brand">
      <span class="brand__mark"></span>
      <div class="brand__name">VOMBRILY</div>
    </div>

    <div class="holder">
      <div class="holder__name">Full Name</div>
      <div class="holder__title">Chief Executive</div>
    </div>
    <span class="divider"></span>
    <ul class="contact">
      <li>
        <svg viewBox="0 0 16 16" aria-hidden="true"><rect x="4" y="1" width="8" height="14" rx="1.5"/><rect x="5.5" y="3" width="5" height="7" fill="#fff"/></svg>
        123-456-7890
      </li>
      <li>
        <svg viewBox="0 0 16 16" aria-hidden="true"><path d="M1 4h14v9H1z"/><path d="M1.5 4.5 8 9.5l6.5-5" stroke="#fff" stroke-width="1.2" fill="none"/></svg>
        first.lastname@vombrily.com
      </li>
    </ul>

    <span class="band-line"></span>
    <span class="band"></span>
  </section>

  <section class="card card--back">
    <div class="brand">
      <span class="brand__mark"></span>
      <div class="brand__name">VOMBRILY</div>
    </div>

    <div class="details">
      <div class="details__block">
        <div class="details__heading">UK address</div>
        <div class="details__line">Vombrily (Europe) Limited Third Floor 58 Corvane Road London N4K 7PQ</div>
      </div>
      <div class="details__block">
        <div class="details__heading">Registered office</div>
        <div class="details__line">9 Ellow Bank Yard London S62 4DT registered in England</div>
      </div>
      <div class="details__reg">Registered In England No. 53xxxx</div>
      <div class="details__web">www.vombrily.com</div>
    </div>
  </section>
</body>
</html>
```